Letterhead Design for Law Firm that Specializes in Property Damage Litigation

We are looking for a redesign of our letterhead. Our current letterhead lists all of our current staff members and we'd like to come up with a design that does NOT list all of the staff members so that it does not need to be updated with every newly hired employee. Must be in editable format.

We are a law firm that specializes in property damage, so we need something that is professional, yet modern. The final design should use our existing logo and should use a blue color scheme (alternate colors would be gray, black, and white).

Industry/Entity Type

Legal

Colors
0054AA
0677BA
7BADD7
CADEEF
E8F1F8

```html
<!DOCTYPE html>
<html lang="en">
<head>
<meta charset="utf-8">
<title>Hartwell Corbin &amp; Lisle Letterhead</title>
<link rel="stylesheet" href="https://fonts.googleapis.com/css2?family=Cinzel:wght@600&family=Montserrat:wght@700&family=Source+Sans+3:wght@400&display=swap">
<style>
  :root {
    --canvas: #e6e7e9;
    --paper: #ffffff;
    --navy: #00305f;
    --gray: #6d6e71;
    --rule-gray: #7a7a7a;
    --white: #ffffff;
  }
  * { margin: 0; padding: 0; box-sizing: border-box; }
  html, body { width: 1200px; height: 829px; overflow: hidden; background: var(--canvas); }
  .canvas { position: relative; width: 1200px; height: 829px; }

  .letterhead {
    --primary: var(--navy);
    --secondary: var(--gray);
    --mark: var(--gray);
    --rule: var(--rule-gray);
    --contact: var(--navy);
    --contact-nj: var(--gray);
    position: absolute; top: 83px; width: 469px; height: 662px;
    background: var(--paper);
    box-shadow: 0 0 14px rgba(0,0,0,0.12);
  }
  .letterhead--blue { left: 83px; }
  .letterhead--mono {
    left: 648px;
    --primary: #000000; --secondary: #222222; --mark: #999999;
    --rule: #999999; --contact: #333333; --contact-nj: #333333;
  }

  .brand-mark {
    position: absolute; left: 30px; top: 40px; width: 30px; height: 30px;
    background: var(--mark);
  }
  .firm-name {
    position: absolute; left: 100px; top: 27px;
    font-family: "Cinzel", Georgia, serif; font-weight: 600;
    font-size: 23px; line-height: 19.6px; letter-spacing: 0;
    color: var(--primary); white-space: nowrap;
  }

  .tagline-band { position: absolute; left: 0; top: 89px; width: 230px; height: 17px; }
  .tagline {
    position: absolute; left: 25px; top: 89px; height: 17px; line-height: 17px;
    font-family: "Montserrat", Arial, sans-serif; font-weight: 700;
    font-size: 7.8px; letter-spacing: 1px; color: var(--white);
    white-space: nowrap;
  }
  .header-rule { position: absolute; left: 231px; right: 0; top: 104px; height: 1.5px; background: var(--rule); }

  .offices { position: absolute; left: 247px; top: 28px; white-space: nowrap; }
  .office-title {
    font-family: "Montserrat", Arial, sans-serif; font-weight: 700;
    font-size: 8.2px; line-height: 10px; letter-spacing: 0.2px;
  }
  .office-line {
    display: flex; align-items: center; gap: 3px;
    font-family: "Source Sans 3", Arial, sans-serif; font-weight: 400;
    font-size: 7.6px; line-height: 8.8px;
  }
  .office-line svg { width: 6px; height: 6px; flex: none; }
  .office--pa .office-title { color: var(--primary); }
  .office--pa .office-line { color: var(--contact); }
  .office--nj { margin-top: 2px; }
  .office--nj .office-title { color: var(--secondary); }
  .office--nj .office-line { color: var(--contact-nj); }

  .footer-rule { position: absolute; left: 0; right: 0; top: 615px; height: 3px; background: var(--primary); }
  .footer-band {
    position: absolute; left: 0; right: 0; top: 620px; bottom: 0;
    background: var(--primary);
    display: flex; align-items: center; justify-content: flex-end; padding-right: 24px;
  }
  .website {
    font-family: "Montserrat", Arial, sans-serif; font-weight: 700;
    font-size: 11px; letter-spacing: 0.3px; color: var(--white);
  }
</style>
</head>
<body>
<div class="canvas">

  <section class="letterhead letterhead--blue">
    <span class="brand-mark"></span>
    <div class="firm-name">HARTWELL<br>CORBIN &amp;<br>LISLE</div>
    <svg class="tagline-band" viewBox="0 0 230 17" preserveAspectRatio="none"><polygon points="0,0 218,0 230,17 0,17" fill="#00305f"/></svg>
    <div class="tagline">THE PROPERTY DAMAGE ATTORNEYS</div>
    <div class="header-rule"></div>
    <div class="offices">
      <div class="office office--pa">
        <div class="office-title">PHILADELPHIA OFFICE</div>
        <div class="office-line"><svg viewBox="0 0 6 6"><circle cx="3" cy="3" r="3" fill="currentColor"/></svg>215.555.0140</div>
        <div class="office-line"><svg viewBox="0 0 6 6"><circle cx="3" cy="3" r="3" fill="currentColor"/></svg>215.555.0192</div>
        <div class="office-line"><svg viewBox="0 0 6 6"><circle cx="3" cy="3" r="3" fill="currentColor"/></svg>2200 Market Street Suite 410 Philadelphia, PA 19103</div>
      </div>
      <div class="office office--nj">
        <div class="office-title">NEW JERSEY OFFICE</div>
        <div class="office-line"><svg viewBox="0 0 6 6"><circle cx="3" cy="3" r="3" fill="currentColor"/></svg>856.555.0133</div>
        <div class="office-line"><svg viewBox="0 0 6 6"><circle cx="3" cy="3" r="3" fill="currentColor"/></svg>215.555.0192</div>
        <div class="office-line"><svg viewBox="0 0 6 6"><circle cx="3" cy="3" r="3" fill="currentColor"/></svg>780 Haddon Avenue Suite 120 Cherry Hill, NJ 08034</div>
      </div>
    </div>
    <div class="footer-rule"></div>
    <div class="footer-band"><span class="website">www.hclpropertylaw.com</span></div>
  </section>

  <section class="letterhead letterhead--mono">
    <span class="brand-mark"></span>
    <div class="firm-name">HARTWELL<br>CORBIN &amp;<br>LISLE</div>
    <svg class="tagline-band" viewBox="0 0 230 17" preserveAspectRatio="none"><polygon points="0,0 218,0 230,17 0,17" fill="#000000"/></svg>
    <div class="tagline">THE PROPERTY DAMAGE ATTORNEYS</div>
    <div class="header-rule"></div>
    <div class="offices">
      <div class="office office--pa">
        <div class="office-title">PHILADELPHIA OFFICE</div>
        <div class="office-line"><svg viewBox="0 0 6 6"><circle cx="3" cy="3" r="3" fill="#000"/></svg>215.555.0140</div>
        <div class="office-line"><svg viewBox="0 0 6 6"><circle cx="3" cy="3" r="3" fill="#000"/></svg>215.555.0192</div>
        <div class="office-line"><svg viewBox="0 0 6 6"><circle cx="3" cy="3" r="3" fill="#000"/></svg>2200 Market Street Suite 410 Philadelphia, PA 19103</div>
      </div>
      <div class="office office--nj">
        <div class="office-title">NEW JERSEY OFFICE</div>
        <div class="office-line"><svg viewBox="0 0 6 6"><circle cx="3" cy="3" r="3" fill="#000"/></svg>856.555.0133</div>
        <div class="office-line"><svg viewBox="0 0 6 6"><circle cx="3" cy="3" r="3" fill="#000"/></svg>215.555.0192</div>
        <div class="office-line"><svg viewBox="0 0 6 6"><circle cx="3" cy="3" r="3" fill="#000"/></svg>780 Haddon Avenue Suite 120 Cherry Hill, NJ 08034</div>
      </div>
    </div>
    <div class="footer-rule"></div>
    <div class="footer-band"><span class="website">www.hclpropertylaw.com</span></div>
  </section>

</div>
</body>
</html>
```